Harbourgate Earthmoving – Website Design Brief

Web Design Brief

We are seeking a web designer to build a modern, responsive website for Harbourgate Earthmoving, a Sydney-based earthworks and excavation company.

2. Project Goal
- Build a professional, easy-to-navigate website that:
- Showcases HGE’s capabilities and past projects
- Attracts residential and commercial developers
- Builds credibility and encourages enquiries

3. Target Audience
- Residential developers and home builders
- Commercial construction firms
- Project managers seeking reliable excavation & plant hire services

4. Services to Highlight
- Bulk Excavation
- Detailed Excavation
- Demolition
- Shoring
- Plant Hire

5. Brand Style & Tone
- Clean, bold, and modern
- Professional with a “we get the job done” attitude
- Colors: Lime Green + Concrete Grey (from logo)
- Fonts: Match the modern, rounded, bold typeface in the logo
- Imagery: Showcase big machines, on-site work, before & after shots

6. Website Pages
Recommended structure:
- Home – Quick intro, project highlights, CTA
- About Us – Team story, mission, safety focus
- Services – Separate sections for each core service
- Projects – Case studies or photo gallery
- Plant Hire – Machines available, specs/photos
- Contact – Form + map + details

7. Assets Provided
- Logo (both long + stacked formats)
- Project photos. More can be provided if required.
- Copy: To be drafted

8. Deliverables
Responsive website (desktop/mobile/tablet)
- SEO-ready structure
- CMS (WordPress) for future edits
- Google Maps integration, job enquiry form

Target Market(s)

Target Audience Residential developers and home builders Commercial construction firms Project managers seeking reliable excavation & plant hire services

Industry/Entity Type

Construction

Number of Pages Required

1 page

Requirements
Must have
• Build a professional, easy-to-navigate website that: Showcases HGE’s capabilities and past projects Attracts residential and commercial developers Builds credibility and encourages enquiries
Nice to have
• All provided in the Description
Should not have

```html
<!DOCTYPE html>
<html lang="en">
<head>
<meta charset="utf-8">
<title>Harbourgate Earthmoving – Earthworks, Excavation &amp; Plant Hire</title>
<link href="https://fonts.googleapis.com/css2?family=Audiowide&family=Poppins:wght@300;400;500;600;700&display=swap" rel="stylesheet">
<style>
:root{
  --lime:#8cc43f;
  --lime-dark:#79b02f;
  --grey-head:#76797c;
  --grey-text:#66696c;
  --ink:#2c2f33;
  --panel:#efefef;
  --white:#ffffff;
  --footer:#2a2e33;
  --star:#ef7a3a;
}
*{margin:0;padding:0;box-sizing:border-box}
html,body{width:1200px;height:4280px;overflow:hidden}
body{font-family:"Poppins",sans-serif;color:var(--grey-text);background:var(--white);position:relative}
section,header,footer{position:relative;width:1200px}
.abs{position:absolute}
a{text-decoration:none;color:inherit}

/* header / hero */
.hero{height:685px;background:linear-gradient(180deg,#34404a 0%,#4d4a3e 30%,#6b5a43 55%,#5a4a36 80%,#3f362b 100%)}
.hero-photo{position:absolute;inset:0;background:radial-gradient(ellipse at 50% 60%,rgba(150,120,80,.55),rgba(30,30,30,.5) 75%)}
.brand{left:105px;top:22px;font-weight:600;font-size:21px;letter-spacing:2.5px;color:var(--lime)}
.nav{font-size:13px;color:#fff}
.nav a{position:absolute;white-space:nowrap}
.nav .active{color:var(--lime)}
.nav-contact{left:1010px;top:20px;width:85px;height:36px;border-radius:18px;background:var(--lime);color:#fff;font-size:13px;display:flex;align-items:center;justify-content:center}
.hero-title{left:0;width:1200px;top:438px;text-align:center;font-family:"Audiowide",sans-serif;font-weight:400;font-size:50px;line-height:60px;color:#fff;letter-spacing:1px}
.hero-title span{color:var(--lime)}
.hero-sub{left:0;width:1200px;top:506px;text-align:center;color:#fff;font-size:16px;letter-spacing:.3px}
.hero-cta{left:503px;top:545px;width:190px;height:42px;border-radius:21px;background:var(--lime);color:#fff;font-size:14px;display:flex;align-items:center;justify-content:center;gap:10px}
.hero-cta i{width:20px;height:20px;border-radius:50%;background:#fff;display:flex;align-items:center;justify-content:center}

/* section headings */
.eyebrow{font-size:11px;color:var(--lime);letter-spacing:.5px;text-transform:uppercase}
.heading{font-size:32px;font-weight:500;color:var(--grey-head);letter-spacing:1.5px;text-transform:uppercase}
.heading b{color:var(--lime);font-weight:500}
.center{left:0;width:1200px;text-align:center}

/* about */
.about{height:608px}
.about-frame{left:127px;top:140px;width:400px;height:375px;background:var(--lime)}
.about-img{left:141px;top:83px;width:442px;height:420px;background:linear-gradient(160deg,#aeb6bd 0%,#8f9aa1 35%,#d8b23a 55%,#6f6a5f 75%,#8b8a86 100%)}
.about-text{left:631px;top:100px;width:440px}
.about-text .heading{margin-top:6px;font-size:28px;line-height:34px}
.about-text p{font-size:12.5px;line-height:21.5px;margin-top:14px}
.btn{background:var(--lime);color:#fff;font-size:12px;font-weight:600;letter-spacing:.5px;display:flex;align-items:center;justify-content:center;gap:8px}
.about-btn{margin-top:22px;width:125px;height:41px}

/* services */
.services{height:635px;background:var(--panel)}
.card{background:#fff;box-shadow:0 3px 10px rgba(0,0,0,.05)}
.svc{top:179px;width:290px;height:365px}
.svc .ph{height:192px}
.svc h3{position:absolute;left:35px;top:218px;font-size:18px;font-weight:500;color:var(--ink)}
.svc p{position:absolute;left:35px;top:256px;width:230px;font-size:11px;line-height:22px}
.svc .more{position:absolute;left:35px;top:313px;font-size:12px;font-weight:600;color:var(--ink);display:flex;align-items:center;gap:8px}
.svc .more.on{color:var(--lime)}
.arrow-btn{width:44px;height:44px;border-radius:50%;display:flex;align-items:center;justify-content:center}

/* projects */
.projects{height:740px}
.gal{position:absolute}

/* testimonials */
.testi{height:574px;background:var(--panel)}
.tcard{top:184px;width:270px;height:246px}
.quote{position:absolute;right:-8px;top:-8px;width:40px;height:40px;border-radius:50%;background:var(--lime);color:#fff;font-size:30px;font-weight:700;display:flex;align-items:center;justify-content:center;line-height:1;padding-top:12px}
.stars{position:absolute;left:22px;top:28px;color:var(--star);font-size:14px;letter-spacing:4px}
.tcard p{position:absolute;left:22px;top:51px;width:235px;font-size:12px;line-height:22.5px;color:var(--ink)}
.avatar{position:absolute;left:22px;top:170px;width:56px;height:56px;border-radius:50%;background:linear-gradient(135deg,#b9a89a,#6c5e57)}
.who{position:absolute;left:92px;top:180px}
.who strong{display:block;font-size:14px;font-weight:600;color:var(--ink)}
.who span{font-size:11px}

/* equipment */
.equip{height:666px}
.eq{top:178px;width:285px;height:323px}
.fleet-btn{left:522px;top:533px;width:156px;height:40px}

/* footer */
.foot{height:372px;background:linear-gradient(180deg,#2f343a,#23272c)}
.foot h4{font-size:14px;font-weight:600;color:#fff;letter-spacing:.5px}
.foot h4::after{content:"";display:block;width:40px;height:2px;background:var(--lime);margin-top:8px}
.foot ul{list-style:none;font-size:12px;color:#fff;line-height:28px;margin-top:8px}
.cinfo{display:flex;gap:10px;color:#fff;font-size:12px;margin-top:14px}
.cinfo strong{display:block;font-size:11px;font-weight:600}
.social{display:flex;align-items:center;gap:10px;color:#fff;font-size:12.5px;margin-top:14px}
.social i{width:28px;height:28px;border-radius:50%;border:1.5px solid #fff;display:block}
.social i.on{background:var(--lime);border-color:var(--lime)}
.foot-brand{left:862px;top:95px;font-weight:700;font-size:33px;line-height:46px;letter-spacing:2px;color:var(--lime)}
.copy{left:0;width:1200px;top:334px;text-align:center;color:#fff;font-size:11px}
.rule{left:141px;top:318px;width:918px;height:1px;background:rgba(255,255,255,.15)}
</style>
</head>
<body>

<header class="hero">
  <div class="hero-photo" role="img" aria-label="Excavation site with excavator beside a suburban house"></div>
  <div class="abs brand">HARBOURGATE EARTHMOVING</div>
  <nav class="abs nav" style="left:0;top:28px;width:1200px">
    <a class="active" style="left:562px">Home</a>
    <a style="left:637px">About Us</a>
    <a style="left:732px">Services</a>
    <a style="left:823px">Projects</a>
    <a style="left:910px">Plant Hire</a>
  </nav>
  <a class="abs nav-contact">Contact</a>
  <h1 class="abs hero-title">WE GET THE <span>JOB DONE</span></h1>
  <p class="abs hero-sub">Reliable, efficient, and safety-focused plant hire and excavation services.</p>
  <a class="abs hero-cta">Get a Free Quote <i><svg width="10" height="10" viewBox="0 0 10 10"><path d="M1 5h7M5 2l3 3-3 3" stroke="#8cc43f" stroke-width="1.6" fill="none"/></svg></i></a>
  <svg class="abs" style="left:697px;top:528px" width="112" height="45" viewBox="0 0 112 45"><path d="M110 2C100 22 70 30 50 28c-8-1-10-10-3-11 7 0 6 12-5 15-12 4-28 5-40 4M2 36l8-5M2 36l8 4" stroke="#fff" stroke-width="1.5" fill="none"/></svg>
</header>

<section class="about">
  <div class="abs about-frame"></div>
  <div class="abs about-img" role="img" aria-label="Excavators and truck on a site with fenced hoarding"></div>
  <div class="abs about-text">
    <div class="eyebrow">Our Story</div>
    <h2 class="heading">About <b>H</b>arbourgate<br><b>E</b>arthmoving</h2>
    <p>Lorem ipsum dolor sit amet, consectetuer adipiscing elit sed diam nonummy nibh euismod tincidunt ut laoreet dolore magna.</p>
    <p style="margin-top:10px">Lorem ipsum dolor sit amet, consectetuer adipiscing elit sed diam nonummy nibh euismod tincidunt ut laoreet dolore mana aliquam erat volutpat. Ut wisi enim ad minim veniam, quis nostrud exerci tation ullamcorper suscipit lobortis nisl ut aliquip ex ea commodo consequat. Duis autem vel eum iriure dolor in henderit in vulputate velit esse molestie consequat vel illum dolore eu fiat nulla facilisis at vero eros et accusan et iusto odio dignissim qui bidit praesent luptatum zzril delenit augue duis dolore te feugait nulla facilisi.</p>
    <a class="btn about-btn">READ MORE <svg width="9" height="9" viewBox="0 0 9 9"><path d="M1 8L8 1M3 1h5v5" stroke="#fff" stroke-width="1.3" fill="none"/></svg></a>
  </div>
</section>

<section class="services">
  <div class="abs center eyebrow" style="top:90px">Who We Serve</div>
  <h2 class="abs center heading" style="top:110px"><b>O</b>ur <b>S</b>ervices</h2>
  <div class="abs arrow-btn" style="left:68px;top:347px;background:#fff"><svg width="10" height="12" viewBox="0 0 10 12"><path d="M7 1L2 6l5 5" stroke="#8cc43f" stroke-width="1.6" fill="none"/></svg></div>
  <article class="abs card svc" style="left:141px">
    <div class="ph" role="img" aria-label="Excavator digging bulk earth beside a building" style="background:linear-gradient(170deg,#7fb2d8 0%,#c9d9e4 35%,#d99a32 60%,#b58a5a 100%)"></div>
    <h3>Bulk Excavation</h3>
    <p>Lorem ipsum dolor sit a consectetuer adipiscing elit sed diam nonummy.</p>
    <a class="more">READ MORE <svg width="9" height="9" viewBox="0 0 9 9"><path d="M1 8L8 1M3 1h5v5" stroke="currentColor" stroke-width="1.3" fill="none"/></svg></a>
  </article>
  <article class="abs card svc" style="left:455px">
    <div class="ph" role="img" aria-label="Shoring trench with timber walls and pipes" style="background:linear-gradient(170deg,#5f7a45 0%,#3c3f3a 40%,#a8824a 75%,#c49a52 100%)"></div>
    <h3>Shoring</h3>
    <p>Lorem ipsum dolor sit a consectetuer adipiscing elit sed diam nonummy.</p>
    <a class="more on">READ MORE <svg width="9" height="9" viewBox="0 0 9 9"><path d="M1 8L8 1M3 1h5v5" stroke="currentColor" stroke-width="1.3" fill="none"/></svg></a>
  </article>
  <article class="abs card svc" style="left:769px">
    <div class="ph" role="img" aria-label="Excavator demolishing a building with rubble" style="background:linear-gradient(170deg,#9fb9d4 0%,#cfd3d2 40%,#d2a93a 55%,#a9a59c 100%)"></div>
    <h3>Demolition</h3>
    <p>Lorem ipsum dolor sit a consectetuer adipiscing elit sed diam nonummy.</p>
    <a class="more">READ MORE <svg width="9" height="9" viewBox="0 0 9 9"><path d="M1 8L8 1M3 1h5v5" stroke="currentColor" stroke-width="1.3" fill="none"/></svg></a>
  </article>
  <div class="abs arrow-btn" style="left:1088px;top:347px;background:var(--lime)"><svg width="10" height="12" viewBox="0 0 10 12"><path d="M3 1l5 5-5 5" stroke="#fff" stroke-width="1.6" fill="none"/></svg></div>
</section>

<section class="projects">
  <div class="abs center eyebrow" style="top:90px">Project Overview</div>
  <h2 class="abs center heading" style="top:110px"><b>O</b>ur <b>P</b>rojects</h2>
  <div class="gal" role="img" aria-label="Workers laying blocks on site" style="left:141px;top:240px;width:255px;height:230px;background:linear-gradient(160deg,#c7cdd1,#6d7a86 50%,#8b8c86)"></div>
  <div class="gal" role="img" aria-label="Demolition excavator breaking a structure" style="left:199px;top:485px;width:197px;height:163px;background:linear-gradient(170deg,#5c8fc8,#a9b6bf 45%,#b79a64 70%,#6a5a46)"></div>
  <div class="gal" role="img" aria-label="Tracked excavator on a levelled dirt site" style="left:407px;top:184px;width:384px;height:395px;background:linear-gradient(180deg,#cfd7dd 0%,#4f6a40 22%,#8c6a4c 45%,#6b5241 75%,#3d3a35 100%)"></div>
  <svg class="gal" style="left:407px;top:184px" width="384" height="395"><rect x="8" y="8" width="367" height="378" fill="none" stroke="#fff" stroke-width="2"/></svg>
  <div class="gal" role="img" aria-label="Excavator beside a tarped site" style="left:802px;top:193px;width:155px;height:138px;background:linear-gradient(170deg,#3b4c5b,#6e5a44 60%,#a57a4e)"></div>
  <div class="gal" role="img" aria-label="Excavator bucket dumping soil" style="left:802px;top:342px;width:257px;height:262px;background:linear-gradient(160deg,#8fae7a,#d7b043 45%,#c59a5d 70%,#7d6a52)"></div>
</section>

<section class="testi">
  <div class="abs center eyebrow" style="top:90px">Project Overview</div>
  <h2 class="abs center heading" style="top:110px"><b>C</b>lient <b>T</b>estimonials</h2>
  <article class="abs card tcard" style="left:141px">
    <div class="quote">”</div><div class="stars">★★★★★</div>
    <p>Ut enim ad minim veniam nostrud exercitation ullamco laboris nisi ut aliquip ex ea commod consequat. Duis aute irure dolor reprehenderit in voluptate velit esse.</p>
    <div class="avatar" role="img" aria-label="Client portrait"></div>
    <div class="who"><strong>Daniel Ashworth</strong><span>Ipsum Dolor</span></div>
  </article>
  <article class="abs card tcard" style="left:465px">
    <div class="quote">”</div><div class="stars">★★★★★</div>
    <p>Ut enim ad minim veniam nostrud exercitation ullamco laboris nisi ut aliquip ex ea commod consequat. Duis aute irure dolor reprehenderit in voluptate velit esse.</p>
    <div class="avatar" role="img" aria-label="Client portrait"></div>
    <div class="who"><strong>Daniel Ashworth</strong><span>Ipsum Dolor</span></div>
  </article>
  <article class="abs card tcard" style="left:778px">
    <div class="quote">”</div><div class="stars">★★★★★</div>
    <p>Ut enim ad minim veniam nostrud exercitation ullamco laboris nisi ut aliquip ex ea commod consequat. Duis aute irure dolor reprehenderit in voluptate velit esse.</p>
    <div class="avatar" role="img" aria-label="Client portrait"></div>
    <div class="who"><strong>Daniel Ashworth</strong><span>Ipsum Dolor</span></div>
  </article>
  <svg class="abs" style="left:553px;top:470px" width="96" height="14" viewBox="0 0 96 14"><path d="M22 7H2M7 2L2 7l5 5" stroke="#999" stroke-width="1.3" fill="none"/><circle cx="35" cy="7" r="1.6" fill="#bbb"/><circle cx="43" cy="7" r="2.2" fill="#8cc43f"/><circle cx="51" cy="7" r="1.6" fill="#bbb"/><circle cx="59" cy="7" r="1.6" fill="#bbb"/><path d="M72 7h20M87 2l5 5-5 5" stroke="#555" stroke-width="1.3" fill="none"/></svg>
</section>

<section class="equip">
  <div class="abs center eyebrow" style="top:96px">Available for Hire</div>
  <h2 class="abs center heading" style="top:116px"><b>E</b>quipment <b>A</b>vailable <b>F</b>or <b>H</b>ire</h2>
  <div class="abs eq" style="left:141px;background:linear-gradient(170deg,#bcd0e2,#e6e9ea 40%,#e0a62c 60%,#a57c52 85%)" role="img" aria-label="Yellow tracked dozer on dirt"></div>
  <div class="abs eq" style="left:457px;background:linear-gradient(170deg,#5d9ad0,#c6d6e2 35%,#e0a940 60%,#b9b3aa 85%)" role="img" aria-label="Excavator loading crushed rock"></div>
  <div class="abs eq" style="left:775px;background:linear-gradient(170deg,#a7aaa9,#d9d5cd 35%,#c8862c 60%,#6e5a47 85%)" role="img" aria-label="Large mining dump truck"></div>
  <a class="abs btn fleet-btn">VIEW FULL FLEET <svg width="9" height="9" viewBox="0 0 9 9"><path d="M1 8L8 1M3 1h5v5" stroke="#fff" stroke-width="1.3" fill="none"/></svg></a>
</section>

<footer class="foot">
  <div class="abs" style="left:141px;top:65px">
    <h4>QUICK LINKS</h4>
    <ul><li>• Home</li><li>• About Us</li><li>• Services</li><li>• Projects</li><li>• Plant Hire</li><li>• Contact Us</li></ul>
  </div>
  <div class="abs" style="left:347px;top:65px;width:240px">
    <h4>CONTACT DETAILS</h4>
    <div class="cinfo"><svg width="12" height="14" viewBox="0 0 12 14"><path d="M6 13S1 8 1 5a5 5 0 0110 0c0 3-5 8-5 8z" fill="#fff"/><circle cx="6" cy="5" r="1.8" fill="#2a2e33"/></svg><div><strong>ADDRESS</strong>123 Ut Wisi Enim Ad Minim<br>Veniam Quis Nostrud.</div></div>
    <div class="cinfo"><svg width="12" height="12" viewBox="0 0 12 12"><path d="M2 1l2.5 0 1 3-1.5 1c.7 1.5 1.8 2.5 3 3l1-1.5 3 1V11c-5 0-9-4-9-10z" fill="#fff"/></svg><div><strong>PHONE</strong>123 456 7890</div></div>
    <div class="cinfo"><svg width="13" height="10" viewBox="0 0 13 10"><rect x="0.5" y="0.5" width="12" height="9" fill="#fff"/><path d="M1 1l5.5 4.5L12 1" stroke="#2a2e33" fill="none"/></svg><div><strong>EMAIL</strong>info@harbourgateearth.com.au</div></div>
  </div>
  <div class="abs" style="left:651px;top:65px">
    <h4>FOLLOW US</h4>
    <div class="social"><i class="on"></i>Social Page</div>
    <div class="social"><i></i>Video Channel</div>
    <div class="social"><i></i>Photo Feed</div>
    <div class="social"><i></i>News Feed</div>
  </div>
  <div class="abs foot-brand">HARBOUR<br>GATE<br>EARTHMOVING</div>
  <div class="abs rule"></div>
  <div class="abs copy">© 2025 HARBOURGATE EARTHMOVING. All Rights Reserved.</div>
</footer>

</body>
</html>
```